Lavoie Roofing

Want a professional looking business card

Industry/Entity Type

Business

Contact Information for Business Card

Mark Lavoie ( Owner) mark@lavoieroofing.example, www.lavoieroofing.example, Adress: 4712 Maple Ridge Road Brookhaven, QC X9Z 4T2

```html
<!DOCTYPE html>
<html lang="en">
<head>
<meta charset="utf-8">
<title>Lavoie Roofing – Business Card</title>
<link href="https://fonts.googleapis.com/css2?family=Arimo:wght@400;700&display=swap" rel="stylesheet">
<style>
  :root {
    --brand-blue: #1d4f95;
    --brand-navy: #17386b;
    --paper: #ffffff;
    --paper-shade: #eef0f2;
    --ink-grey: #5b5f66;
    --ink-dark: #3a3d42;
    --rule-grey: #b9bcc1;
    --backdrop: #2e2f31;
  }
  * { box-sizing: border-box; margin: 0; padding: 0; }
  html, body {
    width: 1200px; height: 997px; overflow: hidden;
    background: var(--backdrop);
    font-family: "Arimo", Arial, sans-serif;
  }
  .stage { position: relative; width: 1200px; height: 997px; }
  .card {
    position: absolute; top: 348px;
    width: 520px; height: 300px;
    border-radius: 18px; overflow: hidden;
  }
  .card-back {
    left: 70px; background: var(--brand-blue);
    display: flex; align-items: center; justify-content: center; gap: 16px;
  }
  .card-back .brand-name {
    color: var(--paper); font-weight: 700; font-size: 50px;
    letter-spacing: 1px; text-transform: uppercase;
  }
  .card-back .brand-square { width: 22px; height: 22px; background: var(--paper); }
  .card-front {
    left: 610px;
    background: linear-gradient(180deg, var(--paper) 0%, var(--paper-shade) 100%);
    text-align: center;
  }
  .front-logo {
    margin-top: 46px;
    display: flex; align-items: center; justify-content: center; gap: 8px;
  }
  .front-logo .brand-name {
    color: var(--brand-navy); font-weight: 700; font-size: 28px;
    letter-spacing: 1px; text-transform: uppercase;
  }
  .front-logo .brand-square { width: 10px; height: 10px; background: var(--brand-navy); }
  .rule { height: 1px; background: var(--rule-grey); margin: 22px 40px 0; }
  .holder-name {
    margin-top: 16px; color: var(--brand-blue);
    font-weight: 700; font-size: 15px; letter-spacing: .5px;
  }
  .holder-role { color: var(--ink-dark); font-weight: 700; font-size: 12px; margin-top: 2px; }
  .contact-icons { display: flex; justify-content: center; gap: 10px; margin-top: 12px; }
  .contact-icons svg { width: 18px; height: 18px; }
  .contact-lines { margin-top: 8px; color: var(--ink-grey); font-size: 13px; line-height: 19px; }
  .web-band {
    position: absolute; left: 0; bottom: 0; width: 100%; height: 30px;
    background: var(--brand-blue); color: var(--paper);
    font-weight: 700; font-size: 13px; letter-spacing: 2px;
    display: flex; align-items: center; justify-content: center;
  }
</style>
</head>
<body>
<main class="stage">
  <section class="card card-back" aria-label="Card back">
    <span class="brand-name">Lavoie Roofing</span>
    <span class="brand-square"></span>
  </section>

  <section class="card card-front" aria-label="Card front">
    <div class="front-logo">
      <span class="brand-name">Lavoie Roofing</span>
      <span class="brand-square"></span>
    </div>
    <div class="rule"></div>
    <p class="holder-name">MARK LAVOIE</p>
    <p class="holder-role">Director</p>
    <div class="contact-icons">
      <svg viewBox="0 0 18 18" aria-label="Phone"><circle cx="9" cy="9" r="9" fill="var(--brand-blue)"/><path d="M6 5.5c.6-.5 1.2-.3 1.5.3l.5 1c.2.4 0 .8-.3 1.1.4.9 1 1.5 1.9 1.9.3-.3.7-.5 1.1-.3l1 .5c.6.3.8.9.3 1.5-1 1-2.6.7-4.3-1S5 6.5 6 5.5z" fill="#fff"/></svg>
      <svg viewBox="0 0 18 18" aria-label="Email"><circle cx="9" cy="9" r="9" fill="var(--brand-blue)"/><rect x="5" y="6" width="8" height="6" fill="none" stroke="#fff" stroke-width="1.2"/><path d="M5 6l4 3.5L13 6" fill="none" stroke="#fff" stroke-width="1.2"/></svg>
      <svg viewBox="0 0 18 18" aria-label="Website"><circle cx="9" cy="9" r="9" fill="var(--brand-blue)"/><path d="M8 10l2-2M7.2 8.2l-1 1a1.6 1.6 0 0 0 2.3 2.3l1-1M10.8 9.8l1-1a1.6 1.6 0 0 0-2.3-2.3l-1 1" fill="none" stroke="#fff" stroke-width="1.2" stroke-linecap="round"/></svg>
    </div>
    <div class="contact-lines">
      <p>5550142287</p>
      <p>mark@lavoieroofing.example</p>
      <p>4712 Maple Ridge Road Brookhaven, QC X9Z 4T2</p>
    </div>
    <div class="web-band">www.lavoieroofing.example</div>
  </section>
</main>
</body>
</html>
```